Tellwick Asset Management - Corporate Letter Head Project

Looking for a classy design based on our current logo. Please find current logo source file in files. With our color scheme.

Target Market(s)

We're an investment firm, the letterhead needs to look professional and attractive to clients.

Industry/Entity Type

Hedgefund

Colors
0054AA
0677BA
7BADD7
CADEEF
E8F1F8

Requirements
Must have
• Our logo, address, phone number, and email

```html
<!DOCTYPE html>
<html lang="en">
<head>
<meta charset="utf-8">
<title>Tellwick Asset Management – Letterhead</title>
<link rel="stylesheet" href="https://fonts.googleapis.com/css2?family=Gelasio:wght@400&display=swap">
<style>
  :root {
    --frame: #d4bec1;
    --paper: #ffffff;
    --navy: #163358;
    --steel: #bac4d2;
    --steel-dark: #a1aab7;
    --serif: "Gelasio", "Palatino Linotype", Georgia, serif;
  }
  * { margin: 0; padding: 0; box-sizing: border-box; }
  html, body { width: 865px; height: 1200px; overflow: hidden; background: var(--frame); }
  .letterhead { position: relative; width: 865px; height: 1200px; background: var(--frame); font-family: var(--serif); }
  .sheet { position: absolute; left: 33px; top: 35px; width: 799px; height: 1130px; background: var(--paper); overflow: hidden; }

  .header-band { position: absolute; left: 0; top: 33px; width: 434px; height: 102px; background: var(--steel); }
  .header-band-shade { position: absolute; left: 138px; top: 33px; width: 12px; height: 102px; background: var(--steel-dark); clip-path: polygon(0 0, 0 100%, 100% 100%); }
  .brand-block { position: absolute; left: 32px; top: 0; width: 107px; height: 158px; background: var(--navy); }
  .brand-mark { position: absolute; left: 46px; top: 48px; width: 79px; height: 79px; border: 1.5px solid #fff; }

  .brand-name { position: absolute; left: 163px; top: 60px; color: var(--navy); font-weight: 400; text-align: center; line-height: 1; }
  .brand-name .line-main { display: block; font-size: 30px; letter-spacing: 0.5px; }
  .brand-name .line-sub { display: block; font-size: 16px; letter-spacing: 11.2px; margin-top: 6px; margin-right: -11px; }

  .contact-list { position: absolute; left: 455px; top: 44px; list-style: none; }
  .contact-item { display: flex; align-items: center; height: 24px; margin-bottom: 5px; color: var(--navy); font-size: 13px; }
  .contact-item svg { width: 24px; height: 24px; margin-right: 11px; flex: none; }

  .margin-rule { position: absolute; left: 32px; top: 158px; width: 383px; height: 943px; border-left: 1px solid var(--navy); border-bottom: 1px solid var(--navy); }
  .footer-bar { position: absolute; left: 415px; top: 1067px; width: 384px; height: 34px; background: var(--navy); }
  .footer-url { position: absolute; left: 448px; top: 1067px; width: 287px; height: 34px; color: #fff; font-size: 17.5px; line-height: 34px; text-align: center; }
  .footer-tab { position: absolute; left: 735px; top: 1050px; width: 41px; height: 80px; background: var(--steel); }
</style>
</head>
<body>
<div class="letterhead">
  <div class="sheet">
    <div class="header-band"></div>
    <div class="header-band-shade"></div>
    <div class="brand-block"></div>
    <div class="brand-mark" aria-hidden="true"></div>

    <div class="brand-name">
      <span class="line-main">TELLWICK ASSET</span>
      <span class="line-sub">MANAGEMENT</span>
    </div>

    <ul class="contact-list">
      <li class="contact-item">
        <svg viewBox="0 0 24 24" aria-hidden="true"><circle cx="12" cy="12" r="12" fill="#163358"/><path d="M6 11.5 12 7l6 4.5" fill="none" stroke="#fff" stroke-width="1.6"/><path d="M8 11v6h3v-3h2v3h3v-6l-4-3z" fill="#fff"/></svg>
        address/office
      </li>
      <li class="contact-item">
        <svg viewBox="0 0 24 24" aria-hidden="true"><circle cx="12" cy="12" r="12" fill="#163358"/><path d="M8.5 6.5c-1 .6-1.5 1.6-1 3 1 2.8 3.6 5.6 6.5 7 1.3.6 2.4.2 3.1-.8l-2-2-1.4.8c-1.4-.8-2.6-2-3.3-3.4l.8-1.4z" fill="#fff"/></svg>
        phone number
      </li>
      <li class="contact-item">
        <svg viewBox="0 0 24 24" aria-hidden="true"><circle cx="12" cy="12" r="12" fill="#163358"/><rect x="6" y="8" width="12" height="8.5" fill="#fff"/><path d="M6 8l6 5 6-5M6 16.5l4.5-4M18 16.5l-4.5-4" fill="none" stroke="#163358" stroke-width="0.9"/></svg>
        email
      </li>
    </ul>

    <div class="margin-rule"></div>
    <div class="footer-bar"></div>
    <div class="footer-url">www.tellwickassetmanagement.com</div>
    <div class="footer-tab"></div>
  </div>
</div>
</body>
</html>
```